TK & LJ Shearing Pty Ltd

We already have an existing logo created by Lumen Guild however we have restructured to a company. We would like someone to add Pty Ltd to our business name please.

Colors

Designer to choose only greyscale colors for use in the design.

```html
<!DOCTYPE html>
<html lang="en">
<head>
<meta charset="utf-8">
<title>TK &amp; LJ Shearing Pty Ltd — Business Card</title>
<link rel="stylesheet" href="https://fonts.googleapis.com/css2?family=Merriweather:wght@400;700&display=swap">
<style>
  :root {
    --stage: #2a2a2c;
    --card-light: #ffffff;
    --card-dark: #2b2b2b;
    --ink-dark: #1c1c1c;
    --ink-light: #f2f2f2;
    --ink-muted: #bdbdbd;
    --icon-bg: #e6e6e6;
  }
  * { margin: 0; padding: 0; box-sizing: border-box; }
  html, body {
    width: 1200px; height: 800px; overflow: hidden;
    background: var(--stage);
    font-family: "Merriweather", Georgia, serif;
  }
  .stage {
    width: 1200px; height: 800px;
    display: flex; align-items: center; justify-content: center; gap: 50px;
  }
  .card {
    width: 525px; height: 300px;
    position: relative;
    box-shadow: 0 14px 30px rgba(0,0,0,.45);
  }
  .card--front {
    background: var(--card-light);
    display: flex; align-items: center; justify-content: center;
  }
  .brand-name {
    font-weight: 700;
    font-size: 27px;
    color: var(--ink-dark);
    letter-spacing: .5px;
    white-space: nowrap;
  }
  .card--back { background: var(--card-dark); color: var(--ink-light); }
  .card--back .brand-name {
    position: absolute; left: 38px; top: 58px;
    color: var(--ink-light);
    font-size: 24px;
  }
  .contact {
    position: absolute; left: 38px; top: 128px;
    font-size: 12px; line-height: 1.55;
  }
  .contact__name { font-weight: 700; font-size: 13.5px; letter-spacing: 1px; }
  .contact__role { color: var(--ink-muted); margin-bottom: 9px; }
  .contact__company { font-weight: 700; }
  .contact__address { color: var(--ink-muted); margin-bottom: 4px; }
  .contact__line { display: flex; align-items: center; gap: 8px; color: var(--ink-muted); }
  .contact__icon { width: 14px; height: 14px; flex: none; }
</style>
</head>
<body>
<main class="stage">
  <section class="card card--front">
    <div class="brand-name">TK &amp; LJ Shearing Pty Ltd</div>
  </section>

  <section class="card card--back">
    <div class="brand-name">TK &amp; LJ Shearing Pty Ltd</div>
    <div class="contact">
      <div class="contact__name">GRANT MERCER</div>
      <div class="contact__role">President</div>
      <div class="contact__company">TK &amp; LJ Shearing Pty Ltd</div>
      <div class="contact__address">PO Box 418 Merredin WA 6415</div>
      <div class="contact__line">
        <svg class="contact__icon" viewBox="0 0 14 14" aria-hidden="true">
          <circle cx="7" cy="7" r="7" fill="var(--icon-bg)"/>
          <rect x="4.5" y="3" width="5" height="8" rx="1" fill="none" stroke="var(--card-dark)" stroke-width="1.2"/>
        </svg>
        <span>Ray 0412 558 190</span>
      </div>
      <div class="contact__line">
        <svg class="contact__icon" viewBox="0 0 14 14" aria-hidden="true">
          <circle cx="7" cy="7" r="7" fill="var(--icon-bg)"/>
          <rect x="3.5" y="4.5" width="7" height="5" fill="none" stroke="var(--card-dark)" stroke-width="1.1"/>
          <path d="M3.5 4.5 L7 7.3 L10.5 4.5" fill="none" stroke="var(--card-dark)" stroke-width="1.1"/>
        </svg>
        <span>tkljshearing@mailbox.com</span>
      </div>
    </div>
  </section>
</main>
</body>
</html>
```